Technology solutions catalog

Were looking for a catalogue to supplement our website and corporate branding.

Our website will give you a good understanding of our products and services as well as our theme.

Our base colour and logo is red, white and grey.

www.voltrane.com.au

The aim of the catalogue is to showcase our business IT services & solutions. This will be a mix of education about the new solutions available to small and medium business today and how these solutions can increase productivity.

We would also like tip sections

This isn't all about selling but also about educating SMB's of the new and exciting IT solutions available today and having them book a free consult with us to discuss further about how we can help the business.

Solutions and area's that the catalogue will need to cover include

Front Cover -
-About us section, with our business contact information (1st page)
- Introduction. (2nd page)
-Communication Solutions - this includes Email, IP phones and business IT networks (2 pages)
- Data & Storage solutions (2 pages)
- Hardware (1 pages)
- Business IT health check list (1 page)
- Services and support offering (2 pages)
- Software & Popular cloud solutions (2 pages)
- Website / E-commerce solutions (2 pages)
Back cover

Based on two pages per solution the whole catalogue will be around 14 pages.

We don't need any text content done. We would like Headings on pages including page numbers. Footer please.

We're looking for a template that we can have our designer finish off by adding in some further product and service image and text.

Thank you for your consideration

Target Market(s)

IT for small and medium businesses

Industry/Entity Type

Supplement

Requirements
Must have
• Size A4
• Design supplied in Adobe indesign so we can edit and add our text and content
• Clean design

```html
<!DOCTYPE html>
<html lang="en">
<head>
<meta charset="utf-8">
<title>Voltrane Catalogue – Communications Spread</title>
<link rel="stylesheet" href="https://fonts.googleapis.com/css2?family=Oswald:wght@500;600&family=Roboto:wght@300;400&display=swap">
<style>
  :root {
    --stage: #e4e4e4;
    --brand-red: #c8242f;
    --ink-grey: #3c3c3c;
    --charcoal: #2a2a2a;
    --charcoal-light: #353535;
    --body-light: #d6d6d6;
    --muted: #9a9a9a;
    --teal: #2b8597;
    --teal-green: #3aa597;
    --amber: #eea12c;
    --paper: #ffffff;
  }
  * { box-sizing: border-box; margin: 0; padding: 0; }
  html, body { width: 1200px; height: 920px; overflow: hidden; background: var(--stage); }
  body { font-family: "Roboto", Arial, sans-serif; }

  .spread {
    position: absolute; left: 34px; top: 60px;
    width: 1132px; height: 800px;
    display: flex;
    box-shadow: 0 10px 30px rgba(0,0,0,.18);
  }
  .page { position: relative; width: 566px; height: 800px; overflow: hidden; }

  /* Left page */
  .page--left { background: var(--paper); }
  .hero-photo {
    position: absolute; inset: 0;
    background: linear-gradient(100deg, #ffffff 0%, #f3f5f7 30%, #dfe5ea 55%, #cdd6dd 75%, #e9edf0 100%);
  }
  .hero-copy { position: absolute; left: 50px; top: 95px; width: 320px; }
  .section-title {
    font-family: "Oswald", "Arial Narrow", sans-serif; font-weight: 600;
    font-size: 50px; line-height: 1; color: var(--brand-red);
    text-transform: uppercase; letter-spacing: .5px;
  }
  .section-lede {
    margin-top: 6px;
    font-weight: 400; font-size: 25px; line-height: 1.18; color: var(--ink-grey);
  }

  /* Right page */
  .page--right { background: linear-gradient(160deg, var(--charcoal-light), var(--charcoal) 60%); }
  .service { position: absolute; left: 55px; display: flex; gap: 30px; width: 470px; }
  .service--network { top: 55px; }
  .service--email { top: 265px; }
  .service--phones { top: 520px; }
  .service__icon {
    flex: 0 0 118px; height: 118px; margin-top: 20px;
    border-radius: 50%;
  }
  .service__icon--network { background: var(--teal); }
  .service__icon--email { background: var(--teal-green); }
  .service__icon--phones { background: var(--amber); }
  .service__heading {
    font-family: "Oswald", "Arial Narrow", sans-serif; font-weight: 500;
    font-size: 22px; color: var(--brand-red); text-transform: uppercase;
    margin-bottom: 8px;
  }
  .service__text { font-size: 12.5px; line-height: 1.45; color: var(--body-light); margin-bottom: 12px; }

  /* Footers */
  .folio { position: absolute; bottom: 22px; display: flex; align-items: center; gap: 10px; font-size: 13px; }
  .folio__number {
    width: 24px; height: 24px; background: var(--brand-red); color: var(--paper);
    display: flex; align-items: center; justify-content: center; font-size: 12px;
  }
  .folio--left { left: 0; }
  .folio--left .folio__contact { color: var(--brand-red); font-weight: 400; }
  .folio--right { right: 0; }
  .folio--right .folio__contact { color: var(--muted); }
</style>
</head>
<body>
  <main class="spread">
    <section class="page page--left">
      <div class="hero-photo" role="img" aria-label="Photo of a smiling businessman using a smartphone beside a bright office window"></div>
      <div class="hero-copy">
        <h1 class="section-title">Communications</h1>
        <p class="section-lede">Keeping in touch with your team and customers at the office or on the road</p>
      </div>
      <footer class="folio folio--left">
        <span class="folio__number">4</span>
        <span class="folio__contact">1300 555 019</span>
      </footer>
    </section>

    <section class="page page--right">
      <article class="service service--network">
        <div class="service__icon service__icon--network" role="img" aria-label="Round illustration of networked computer devices"></div>
        <div class="service__body">
          <h2 class="service__heading">Network</h2>
          <p class="service__text">Having a fast, reliable and secure business network is extremely important to be competitive and ensure your IT can operate.</p>
          <p class="service__text">Voltrane offers a range of network services and support options.</p>
        </div>
      </article>

      <article class="service service--email">
        <div class="service__icon service__icon--email" role="img" aria-label="Round illustration of email and messaging on a computer"></div>
        <div class="service__body">
          <h2 class="service__heading">Email &amp; Collaboration</h2>
          <p class="service__text">Email is the way we communicate to our team and customers, but not all email services are the same or provide the same benefits.</p>
          <p class="service__text">Security, spam and access on mobile devices is where we can help your business.</p>
          <p class="service__text">Voltrane offers Nimbus Suite, a leading email and collaboration suite that improves productivity while allowing access to your email, calendars and messages while in or out of the office.</p>
        </div>
      </article>

      <article class="service service--phones">
        <div class="service__icon service__icon--phones" role="img" aria-label="Round illustration of a hand using a touchscreen phone"></div>
        <div class="service__body">
          <h2 class="service__heading">Office Phones</h2>
          <p class="service__text">With your internet service you can have office phones that can call local, national and mobiles at heavily discounted rates.</p>
          <p class="service__text">Using the internet offers many great phone features such as message to email. Attended call transferring and out of hours messages when calling outside your normal trading hours.</p>
        </div>
      </article>

      <footer class="folio folio--right">
        <span class="folio__contact">www.voltrane.com.au</span>
        <span class="folio__number">5</span>
      </footer>
    </section>
  </main>
</body>
</html>
```